Business cards and Stationary | Lumora Music Events

Hello! We need business cards and stationery for a new small business in the music industry. "Lumora is a high-end music agency which provides an unparalleled level of talent and personalized service to the realm entertainment, corporate events, and luxury weddings. Here is where the classical meets the contemporary and we can bring your vision to life.Keeping a steady finger on the pulse of current trends and consistently raising the bar for industry standards, Lumora continues to rise to the forefront of the music industry, providing the utmost professional, high-end, elegant, and engaging entertainment in Australia and World-Wide."

Target Market(s)

Class A. high profile corporate business.

Industry/Entity Type

Entertainment

Contact Information for Business Card

Lumora Music Events

Clare Yoshinaga
Director | Violinist

Level 7, 41 Caddow Lane
Sydney, 2000

Website: www.lumoramusicevents-demo.net
Phone number: 0455 318 602
Email: clare@lumoramusicevents-demo.net

Font styles to use
Serif
Sans Serif
Script

Colors
feeeee
0355a3
f59296
ffffff

Requirements
Nice to have
• Clean and sophisticated would be perfect.
• If there is a way to include the Instagram without being tacky, that would be awesome
• @lumoramusicevents
• Our website and logo have the following fonts:
• The primary logo is inspired and based on a font called BillionScript but the B is completely hand drawn and the rest is customised a bit to work together cohesively
• Monserrat Light - Is the Music part of the logo and as headers in the site
• Open Sans 300 and 400 (Light or Regular) is used mostly as the body text in the site
• If you want to access the website:
• www.lumoramusicevents-demo.net
• username: client
• password: preview

```html
<!DOCTYPE html>
<html lang="en">
<head>
<meta charset="utf-8">
<title>Lumora Music Events – Stationery</title>
<link href="https://fonts.googleapis.com/css2?family=Open+Sans:ital,wght@0,400;0,600;1,400&family=Montserrat:wght@300;400&display=swap" rel="stylesheet">
<style>
  :root {
    --backdrop: #838387;
    --paper: #ffffff;
    --charcoal: #3b3a3c;
    --blush: #f48f94;
    --rose: #c28a89;
    --ink: #4a4a4c;
    --ink-strong: #333335;
  }
  * { margin: 0; padding: 0; box-sizing: border-box; }
  html, body { width: 1200px; height: 1194px; overflow: hidden; }
  body {
    position: relative;
    background: var(--backdrop);
    font-family: "Open Sans", sans-serif;
    color: var(--ink);
  }
  .sheet, .card { position: absolute; overflow: hidden; }
  .letterhead {
    left: 91px; top: 119px; width: 692px; height: 979px;
    background: var(--paper);
  }
  .wordmark {
    position: absolute;
    display: flex; align-items: center; gap: 7px;
    font-family: "Montserrat", sans-serif;
    font-weight: 300;
    letter-spacing: 2px;
    white-space: nowrap;
  }
  .wordmark .dot {
    width: 6px; height: 6px; border-radius: 50%;
    background: currentColor;
    flex: none;
  }
  .letterhead .wordmark {
    right: 36px; top: 92px; font-size: 15px; color: var(--rose);
  }
  .footer-name {
    position: absolute; left: 96px; top: 918px;
    font-size: 16px; font-weight: 600; letter-spacing: 1.6px;
    color: var(--ink); white-space: nowrap;
  }
  .footer-mark {
    position: absolute; left: 74px; top: 925px;
    width: 7px; height: 7px; border-radius: 50%; background: var(--rose);
  }
  .contact {
    position: absolute;
    font-size: 7.8px; line-height: 11.6px;
    color: var(--ink);
    white-space: nowrap;
  }
  .contact li { list-style: none; display: flex; align-items: center; gap: 4px; }
  .contact b { font-weight: 600; color: var(--ink-strong); }
  .contact .bullet {
    width: 6px; height: 6px; border-radius: 50%; background: var(--ink-strong);
    margin: 0 1px; flex: none;
  }
  .contact svg { width: 8px; height: 8px; fill: var(--ink-strong); flex: none; }
  .letterhead .contact-online { left: 391px; top: 912px; }
  .letterhead .contact-office { left: 562px; top: 912px; }

  .card { left: 814px; width: 284px; height: 171px; }
  .card-dark { top: 526px; background: var(--charcoal); }
  .card-details { top: 724px; background: var(--paper); }
  .card-blush { top: 922px; background: var(--blush); }
  .card .wordmark { left: 50%; top: 50%; transform: translate(-50%, -50%); font-size: 16px; }
  .card-dark .wordmark { color: #d8a4a6; }
  .card-blush .wordmark { color: var(--paper); }

  .person { position: absolute; left: 168px; top: 50px; white-space: nowrap; }
  .person-name {
    font-size: 15px; font-weight: 600; letter-spacing: 1.8px; color: var(--ink);
    line-height: 18px;
  }
  .person-role {
    font-size: 7.6px; font-style: italic; letter-spacing: .4px;
    color: var(--ink); margin-left: 6px;
  }
  .card-details .contact { font-size: 7px; line-height: 11.4px; }
  .card-details .contact-online { left: 18px; top: 116px; }
  .card-details .contact-office { left: 182px; top: 116px; }
</style>
</head>
<body>

<section class="sheet letterhead" aria-label="Letterhead">
  <div class="wordmark"><span class="dot"></span>Lumora Music</div>

  <span class="footer-mark"></span>
  <p class="footer-name">Lumora Music Events</p>

  <ul class="contact contact-online">
    <li><span class="bullet"></span>lumoramusicevents</li>
    <li><span class="bullet"></span>Lumora Music Events</li>
    <li><b>E:</b> contact@lumoramusicevents-demo.net</li>
    <li><b>www.lumoramusicevents-demo.net</b></li>
  </ul>
  <ul class="contact contact-office">
    <li><b>P:</b> 0455 318 602</li>
    <li><svg viewBox="0 0 24 24" aria-hidden="true"><path d="M6.6 10.8a15.1 15.1 0 0 0 6.6 6.6l2.2-2.2a1 1 0 0 1 1-.25 11.4 11.4 0 0 0 3.6.57 1 1 0 0 1 1 1V20a1 1 0 0 1-1 1A17 17 0 0 1 3 4a1 1 0 0 1 1-1h3.5a1 1 0 0 1 1 1c0 1.25.2 2.45.57 3.57a1 1 0 0 1-.25 1z"/></svg>0455 318 602</li>
    <li>Level 7, 41 Caddow Lane</li>
    <li>Sydney, 2000</li>
  </ul>
</section>

<section class="card card-dark" aria-label="Business card front, dark">
  <div class="wordmark"><span class="dot"></span>Lumora Music</div>
</section>

<section class="card card-details" aria-label="Business card back">
  <div class="person">
    <p class="person-name">JOHN DOE</p>
    <p class="person-role">Business Associates</p>
  </div>
  <ul class="contact contact-online">
    <li><span class="bullet"></span>lumoramusicevents</li>
    <li><span class="bullet"></span>Lumora Music Events</li>
    <li><b>E:</b> contact@lumoramusicevents-demo.net</li>
    <li><b>www.lumoramusicevents-demo.net</b></li>
  </ul>
  <ul class="contact contact-office">
    <li><b>P:</b> 0455 318 602</li>
    <li><svg viewBox="0 0 24 24" aria-hidden="true"><path d="M6.6 10.8a15.1 15.1 0 0 0 6.6 6.6l2.2-2.2a1 1 0 0 1 1-.25 11.4 11.4 0 0 0 3.6.57 1 1 0 0 1 1 1V20a1 1 0 0 1-1 1A17 17 0 0 1 3 4a1 1 0 0 1 1-1h3.5a1 1 0 0 1 1 1c0 1.25.2 2.45.57 3.57a1 1 0 0 1-.25 1z"/></svg>0455 318 602</li>
    <li>Level 7, 41 Caddow Lane</li>
    <li>Sydney, 2000</li>
  </ul>
</section>

<section class="card card-blush" aria-label="Business card front, blush">
  <div class="wordmark"><span class="dot"></span>Lumora Music</div>
</section>

</body>
</html>
```